IT consulting company looking for a modern business design for a website and a new logo

We are the IT-consulting company VendiMark from Germany and need a new and modern business website and a new logo. We are specialized in output management. Our services include business analysis, outsourcing, development, training and project leading. We wish for a design with nature pictures (mountains, lakes, rivers, forests, etc.) for our company with the colors green and blue. If it is possible, a slow-mo video of a nature scene. The design should be responsive and the menu should change to a hamburger menu. The following are: • Services / Solutions 1. Output Management 2. Outsourcing 3. Development 4. Business Analyst 5. Training • Partners • Careers • About Us 1. Project A 2. Project B 3. Project C • Contact Notes for the following categories: For "Services / Solutions" we want to conclude some contents from all the sub-points and sub-points below. Additionally, we would like to see some sub-point under "Services / Solutions". For Output Management: "5 Benefits of Output Management Systems (OMS) - OMS Simplifies and Accelerates External Communication - Helps Reduce Communication Mistakes - Provides Customers With Fast and Secure Responses to your questions - Employees can focus on the essential as they can access prepared templates - Companies get complete transparency about their communication "The point" partner does not have sub-points. The content here is a quote and the logo from the company Brel. For now, just placeholders on this site. The next point wants to be "career" without sub-point and wants to contain some text. Carrer options wants to be listed here. Next point wants to be "About us", where we need sub-points which we do not know exactly at this moment, but they will contain text. By clicking directly on "About us" we want to include pictures and texts about 6 employees for which we only need placeholders at the moment. The last point wants to be "contact", where customers can send us messages. The main page should include a story about our company, which can be a placeholder for now. For reference, designs have a look at: https://brelvantix.de/ https://www.lumortika.com/ https://www.tpvrano.de/ We prefer WordPress designs, created with the plugin ELEMENTOR, so that we can easily edit the content by ourselves. The final design should look professional, competent and modern.

Target Market(s)

With our website, we want to reach the following target groups. <br> <br> <br> <br> <br> <br> <br> <br> <br> <br> <br> <br> <br> <br> <br> <br> <br> <br> <br> <br> <br> <br> <br> <br> <br> <br> <br> <br> <br> <br> <br> <br> <br> <br> <br> <br> <br> <br> <br> <br> <br> <br> <br> <br> <br> <br> <br> <br> <br>

Industry/Entity Type

Consulting

Logo Text

(optionally) VendiMark

Font styles to use
Sans Serif

Colors

Designer to choose colors to be used in the design.

Requirements
Must have
• 1. Outsourcing 3. Development 4. Business Analyst 5. Training • Partners • Careers • About Us 1. Project A 2. Project B 3. Project C • Contact The above-mentioned background picture with nature motifs (mountains, lakes, rivers, forests, etc.). WordPress design in primary colors blue and green.
Nice to have
• ELEMENTOR template. Effects for the background pictures. Counter of all successful projects for Output Management, Business Analyst and Training

```html
<!DOCTYPE html>
<html lang="en">
<head>
<meta charset="utf-8">
<title>VendiMark Consulting</title>
<link href="https://fonts.googleapis.com/css2?family=Poppins:wght@300;400;500;600;700&display=swap" rel="stylesheet">
<style>
:root{
  --blue:#1b6fd3;
  --blue-dark:#1459ad;
  --green:#4fbf1d;
  --ink:#222428;
  --body:#5b5f66;
  --light:#f3f4f6;
  --line:#dfe2e6;
  --footer:#2a2c30;
  --white:#fff;
}
*{margin:0;padding:0;box-sizing:border-box}
html,body{width:1200px;height:4875px;overflow:hidden}
body{font-family:'Poppins',sans-serif;color:var(--ink);background:var(--white);position:relative}
.abs{position:absolute}
.para{font-size:10.5px;line-height:19px;color:var(--body)}
.center{text-align:center}
.section-title{font-size:35px;font-weight:600;color:var(--ink);text-align:center;width:1200px;left:0}
.section-sub{width:1200px;left:0;text-align:center}
.btn{display:flex;align-items:center;justify-content:center;color:#fff;font-size:11px;font-weight:600}
.btn-blue{background:var(--blue)}
.btn-green{background:var(--green)}
.ph{position:absolute}

/* header */
.header{top:0;left:0;width:1200px;height:95px;background:#fff}
.brand{left:95px;top:22px;display:flex;align-items:center;gap:10px}
.brand-mark{width:44px;height:44px;border-radius:50%;background:var(--blue)}
.brand-name{font-size:19px;font-weight:600;color:var(--blue)}
.support{right:95px;top:14px;font-size:11px;font-weight:500;display:flex;align-items:center;gap:6px}
.support span{color:var(--blue)}
.nav{left:259px;top:43px;width:613px;height:52px}
.nav ul{position:absolute;left:0;top:0;width:613px;height:52px;list-style:none;display:flex;align-items:center;justify-content:center;gap:0;padding-left:40px}
.nav li{color:#fff;font-size:11px;padding:0 30px;position:relative}
.nav li+li::before{content:"";position:absolute;left:0;top:3px;width:1px;height:10px;background:#fff}
.cta-top{left:872px;top:43px;width:328px;height:52px;font-size:14px}

/* hero */
.hero{top:95px;left:0;width:1200px;height:541px;background:linear-gradient(180deg,#5d6e7e 0%,#8c9aa4 30%,#4d5a4a 55%,#24321f 80%,#1a2414 100%)}
.hero-title{left:92px;top:140px;color:#fff;line-height:72px}
.hero-title .l1{font-size:60px;font-weight:400;display:block}
.hero-title .l2{font-size:64px;font-weight:600;display:block}
.hero-text{left:95px;top:292px;width:520px;color:#fff;font-size:10.5px;line-height:19px}
.hero-btns{left:95px;top:344px;display:flex;gap:10px}
.hero-btns .btn{height:32px;padding:0 20px}
.slider-dots{left:1133px;top:193px;display:flex;flex-direction:column;align-items:center;gap:12px}
.dot{width:10px;height:10px;border-radius:50%;background:#fff}
.dot.active{width:20px;height:20px;border:2px solid #fff;background:transparent;display:flex;align-items:center;justify-content:center}
.dot.active::after{content:"";width:8px;height:8px;border-radius:50%;background:#fff}
.slider-line{width:2px;height:70px;background:rgba(255,255,255,.6)}
.slide-count{left:1118px;top:362px;color:#fff;font-size:14px;font-weight:600}
.slide-count small{font-size:10px;font-weight:400}

/* info strip */
.info{top:636px;left:0;width:1200px;height:227px;background:var(--light)}
.info-item{top:0;height:227px;width:340px;display:flex;flex-direction:column;align-items:center;justify-content:center}
.info-label{font-size:23px;font-weight:400;color:var(--ink);margin-top:8px}
.info-value{font-size:23px;font-weight:600;color:var(--blue);margin-top:2px}

/* about */
.about-stats{top:1340px;left:0;width:1200px;height:331px;background:linear-gradient(110deg,#2d3440 0%,#4b5260 40%,#6a6f74 60%,#2e333b 100%)}
.project{top:1130px;width:320px;height:250px;background:#fff;border-radius:0 0 14px 14px;box-shadow:0 6px 22px rgba(0,0,0,.12);text-align:center}
.project h3{font-size:20px;font-weight:600;margin-top:70px}
.project .para{width:240px;margin:10px auto 0;font-size:10px;line-height:19px}
.project a{display:block;margin-top:12px;color:var(--blue);font-size:11px;font-weight:600}
.project.featured{top:1120px;background:var(--blue);height:250px;border-radius:0}
.project.featured h3,.project.featured .para,.project.featured a{color:#fff}
.diamond{left:50%;width:76px;height:76px;margin-left:-38px;top:-42px;transform:rotate(45deg);background:var(--blue);display:flex;align-items:center;justify-content:center}
.diamond svg{transform:rotate(-45deg)}
.notch{left:50%;top:-1px;margin-left:-40px;width:80px;height:48px}
.stat{top:1490px;display:flex;align-items:center;gap:10px;color:#fff}
.stat-num{font-size:38px;font-weight:600;line-height:38px}
.stat-num small{font-size:18px}
.stat-label{font-size:20px;font-weight:600;line-height:22px}
.stat-div{top:1495px;width:1px;height:70px;background:rgba(255,255,255,.4)}

/* services */
.service{top:1898px;width:170px;text-align:center}
.service h4{font-size:15px;font-weight:600;margin-top:20px}
.service .para{font-size:10px;line-height:19.5px;margin-top:8px}
.service .btn{width:112px;height:32px;margin:14px auto 0}

/* career */
.career{top:2341px;left:0;width:1200px;height:668px;background:var(--light)}
.video{top:2424px;left:95px;width:558px;height:500px;background:linear-gradient(135deg,#3d4045 0%,#5d6166 45%,#2b2d31 100%)}
.play{left:320px;top:2618px;width:112px;height:112px;border-radius:50%;border:3px solid #fff;background:rgba(0,0,0,.35);display:flex;align-items:center;justify-content:center}
.career-box{top:2472px;left:572px;width:628px;height:410px;background:#fff;padding:60px 55px 0 54px}
.career-box h2{font-size:32px;font-weight:500}
.career-box .para{margin-top:14px;font-size:10.5px;line-height:19.5px}
.career-box a{display:block;margin-top:10px;color:var(--blue);font-size:11px;font-weight:600}

/* news */
.news{top:3191px;width:320px;height:410px;background:#fff;box-shadow:0 4px 18px rgba(0,0,0,.1)}
.news-img{width:320px;height:206px;background:linear-gradient(135deg,#c9cdd2,#8b939b 60%,#5b636b)}
.news-body{padding:22px 45px 0 45px;height:204px}
.news-date{font-size:10px;color:var(--blue);font-weight:600;padding-top:14px;border-left:1px solid var(--blue);padding-left:0;position:relative}
.news-body h5{font-size:14px;font-weight:600;margin-top:10px}
.news-body .para{font-size:9.5px;line-height:18px;margin-top:4px}
.news-body .btn{width:82px;height:26px;font-size:10px;margin-top:10px}

/* request */
.request-photo{top:3709px;left:640px;width:560px;height:540px;background:linear-gradient(90deg,rgba(255,255,255,1) 0%,rgba(220,225,230,.6) 20%,#b9c2cc 45%,#7e8c99 75%,#5f6d7b 100%)}
.request-title{left:95px;top:3790px;font-size:38px;font-weight:500}
.request-sub{left:95px;top:3843px;font-size:11.5px;color:var(--body)}
.field{height:44px;border:1px solid var(--line);background:#fff;font-size:9.5px;color:#9aa0a6;padding:0 16px;display:flex;align-items:center;justify-content:space-between}
.field.area{align-items:flex-start;padding-top:14px}
.send{left:95px;top:4150px;width:284px;height:44px;font-size:14px;font-weight:500}
.call-alt{left:398px;top:4164px;font-size:12px;color:var(--body)}
.call-alt span{color:var(--blue)}

/* partners */
.partners{top:4249px;left:0;width:1200px;height:189px;background:#fff}
.arrow-btn{top:4332px;width:26px;height:26px;border-radius:50%;border:1px solid #c8ccd0;display:flex;align-items:center;justify-content:center}
.partner-row{left:100px;top:4328px;width:1000px;display:flex;justify-content:space-between;align-items:center}
.partner-shape{height:22px;background:#c9cdd1;border-radius:3px}

/* footer */
.footer{top:4438px;left:0;width:1200px;height:437px;background:var(--footer);color:#fff}
.foot-h{font-size:15px;font-weight:600;color:#fff}
.foot-text{font-size:10px;line-height:19px;color:#d6d8db}
.foot-list{list-style:none;font-size:10.5px;line-height:30px;color:#d6d8db}
.contact-row{display:flex;gap:12px;align-items:flex-start;font-size:10px;line-height:17px;color:#d6d8db;margin-bottom:12px}
.mini-news{display:flex;gap:14px;margin-bottom:10px}
.mini-thumb{width:80px;height:48px;background:linear-gradient(135deg,#8d949b,#4e555c)}
.mini-news p{font-size:10px;line-height:15px;color:#e6e7e9;margin-top:8px}
.mini-news small{display:block;font-size:9px;color:#a6aaaf}
.follow{left:95px;top:4650px;display:flex;align-items:center;gap:18px;font-size:17px;font-weight:600}
.social{width:12px;height:12px;border-radius:50%;background:#d6d8db}
.copyright{left:0;top:4795px;width:1200px;border-top:1px solid rgba(255,255,255,.12);padding-top:18px;text-align:center;font-size:10.5px;color:#d6d8db}
</style>
</head>
<body>

<!-- header -->
<header class="abs header">
  <div class="abs brand"><div class="brand-mark"></div><div class="brand-name">VendiMark</div></div>
  <div class="abs support">
    <svg width="16" height="16" viewBox="0 0 16 16"><circle cx="8" cy="8" r="6.5" fill="none" stroke="#1b6fd3" stroke-width="1.5"/><path d="M8 4v4l3 2" stroke="#1b6fd3" stroke-width="1.5" fill="none"/></svg>
    24/7 Support : <span>+123-456-7890</span>
  </div>
  <nav class="abs nav">
    <svg class="abs" width="613" height="52" style="left:0;top:0"><polygon points="30,0 613,0 613,52 0,52" fill="#1b6fd3"/></svg>
    <ul><li>About Us</li><li>Services</li><li>Partner</li><li>Career</li><li>Contact</li></ul>
  </nav>
  <div class="abs btn btn-green cta-top">Free Consultation</div>
</header>

<!-- hero -->
<section class="abs hero" role="img" aria-label="Mountain valley with pine forest under a cloudy sky"></section>
<h1 class="abs hero-title"><span class="l1">Marketing &amp;</span><span class="l2">Public Relations</span></h1>
<p class="abs hero-text">We deliver high impact Public Relations, search and social campaigns for technology, telecoms and high growth companies. Our solutions work and bring amazing results.</p>
<div class="abs hero-btns"><div class="btn btn-blue">know More</div><div class="btn btn-green">Contact Us</div></div>
<div class="abs slider-dots"><div class="dot active"></div><div class="dot"></div><div class="dot"></div><div class="slider-line"></div></div>
<div class="abs slide-count">01 <small>/ 03</small></div>

<!-- info strip -->
<section class="abs info">
  <svg class="abs" width="1200" height="227" style="left:0;top:0"><polygon points="398,0 730,0 810,227 470,227" fill="#fff"/></svg>
  <div class="abs info-item" style="left:68px">
    <svg width="34" height="44" viewBox="0 0 34 44"><path d="M17 2C9 2 3 8 3 16c0 10 14 24 14 24s14-14 14-24C31 8 25 2 17 2z" fill="none" stroke="#1b6fd3" stroke-width="3"/><circle cx="17" cy="16" r="5" fill="#1b6fd3"/><ellipse cx="17" cy="41" rx="9" ry="2" fill="#1b6fd3"/></svg>
    <div class="info-label">Address</div><div class="info-value">CA Lorem,80 Germany</div>
  </div>
  <div class="abs info-item" style="left:430px">
    <svg width="38" height="38" viewBox="0 0 38 38"><path d="M8 6l6 0 3 8-4 3c2 4 5 7 9 9l3-4 8 3v6c0 2-2 3-4 3C16 33 5 22 5 9c0-2 1-3 3-3z" fill="#1b6fd3"/><path d="M22 4a12 12 0 0 1 12 12M22 10a6 6 0 0 1 6 6" stroke="#1b6fd3" stroke-width="2.5" fill="none"/></svg>
    <div class="info-label">Call Us</div><div class="info-value">+123-456-7890</div>
  </div>
  <div class="abs info-item" style="left:784px">
    <svg width="34" height="34" viewBox="0 0 34 34"><path d="M3 14l14-11 14 11v17H3z" fill="#1b6fd3"/><rect x="8" y="8" width="18" height="12" fill="#fff"/><path d="M11 12h12M11 16h8" stroke="#1b6fd3" stroke-width="1.5"/><path d="M3 14l14 10 14-10" fill="none" stroke="#fff" stroke-width="1.5"/></svg>
    <div class="info-label">Have Any Question?</div><div class="info-value">mail@vendimark-mail.de</div>
  </div>
</section>

<!-- about -->
<h2 class="abs section-title" style="top:945px">About Us</h2>
<p class="abs section-sub para" style="top:1000px">Lorem Ipsum is simply dummy text of the printing and typesetting industry. Lorem Ipsum has<br>been the industry's standard dummy text ever since the 1500s.</p>

<div class="abs about-stats" role="img" aria-label="Two business people in conversation in a modern lounge"></div>

<article class="abs project" style="left:95px">
  <div class="abs diamond"><svg width="34" height="34" viewBox="0 0 34 34" fill="none" stroke="#fff" stroke-width="2"><circle cx="17" cy="17" r="13"/><circle cx="17" cy="17" r="8"/><circle cx="17" cy="17" r="3" fill="#fff"/><path d="M17 17l13-13"/></svg></div>
  <h3>Project A</h3>
  <p class="para">Lorem Ipsum is simply dummy text of the printing and typesetting industry. Lorem Ipsum has been the industry's standard dummy text ever since the 1500s.</p>
  <a>Know More &gt;&gt;</a>
</article>
<article class="abs project featured" style="left:441px">
  <svg class="abs notch" viewBox="0 0 80 48"><polygon points="0,0 80,0 40,44" fill="#fff"/><circle cx="40" cy="12" r="11" fill="none" stroke="#1b6fd3" stroke-width="1.5" stroke-dasharray="3 2"/><path d="M34 16v-4M38 16v-7M42 16v-5M46 16v-8" stroke="#1b6fd3" stroke-width="2"/></svg>
  <h3 style="margin-top:72px">Project B</h3>
  <p class="para">Lorem Ipsum is simply dummy text of the printing and typesetting industry. Lorem Ipsum has been the industry's standard dummy text ever since the 1500s.</p>
  <a>Know More &gt;&gt;</a>
</article>
<article class="abs project" style="left:787px">
  <div class="abs diamond"><svg width="34" height="34" viewBox="0 0 34 34" fill="none" stroke="#fff" stroke-width="2"><circle cx="17" cy="17" r="13"/><path d="M17 4v26M4 17h26M8 8c6 5 12 5 18 0M8 26c6-5 12-5 18 0"/></svg></div>
  <h3>Project C</h3>
  <p class="para">Lorem Ipsum is simply dummy text of the printing and typesetting industry. Lorem Ipsum has been the industry's standard dummy text ever since the 1500s.</p>
  <a>Know More &gt;&gt;</a>
</article>

<div class="abs stat" style="left:140px">
  <svg width="40" height="42" viewBox="0 0 40 42" fill="none" stroke="#fff" stroke-width="2"><rect x="4" y="4" width="26" height="34"/><path d="M10 12h14M10 19h14M10 26h10"/><path d="M34 8v26"/></svg>
  <div><div class="stat-num">1.5<small>k</small></div><div class="stat-label">Projects</div></div>
</div>
<div class="abs stat-div" style="left:338px"></div>
<div class="abs stat" style="left:395px">
  <svg width="36" height="42" viewBox="0 0 36 42" fill="none" stroke="#fff" stroke-width="2"><circle cx="18" cy="15" r="12"/><circle cx="18" cy="15" r="6"/><path d="M10 25l-4 14 7-4 5 5 2-12M26 25l4 14-7-4"/></svg>
  <div><div class="stat-num">25</div><div class="stat-label">Awards</div></div>
</div>
<div class="abs stat-div" style="left:582px"></div>
<div class="abs stat" style="left:630px">
  <svg width="44" height="42" viewBox="0 0 44 42" fill="none" stroke="#fff" stroke-width="2"><circle cx="12" cy="8" r="4"/><path d="M6 24v-8h12v8M12 24v14"/><path d="M22 10h18M22 18h14M22 26h18M22 34h12"/></svg>
  <div><div class="stat-num">81</div><div class="stat-label">Professionals</div></div>
</div>
<div class="abs stat-div" style="left:866px"></div>
<div class="abs stat" style="left:918px">
  <svg width="42" height="42" viewBox="0 0 42 42" fill="none" stroke="#fff" stroke-width="2"><circle cx="21" cy="22" r="16"/><path d="M13 25c4 6 12 6 16 0"/><circle cx="15" cy="18" r="1.5" fill="#fff"/><circle cx="27" cy="18" r="1.5" fill="#fff"/><path d="M6 6l4 4M36 6l-4 4"/></svg>
  <div><div class="stat-num">99%</div><div class="stat-label">Satisfied</div></div>
</div>

<!-- services -->
<h2 class="abs section-title" style="top:1762px">Our Services</h2>
<p class="abs section-sub para" style="top:1817px">Lorem Ipsum is simply dummy text of the printing and typesetting industry. Lorem Ipsum has<br>been the industry's standard dummy text ever since the 1500s.</p>

<div class="abs service" style="left:112px">
  <svg width="140" height="140" viewBox="0 0 140 140"><circle cx="70" cy="70" r="66" fill="#fff" stroke="#e6e8eb" stroke-width="2"/><path d="M4 70a66 66 0 0 1 132 0" fill="none" stroke="#1b6fd3" stroke-width="5"/><circle cx="70" cy="58" r="12" fill="none" stroke="#1b6fd3" stroke-width="3"/><circle cx="70" cy="58" r="4" fill="#1b6fd3"/><path d="M46 98c0-14 10-22 24-22s24 8 24 22z" fill="#1b6fd3"/></svg>
  <h4>Output Management</h4>
  <p class="para">Lorem Ipsum is simply dummy text of the printing and typesetting industry. Lorem Ipsum has been the industry's standard dummy text ever since the 1500s.</p>
  <div class="btn btn-blue">View Details</div>
</div>
<div class="abs service" style="left:313px">
  <svg width="140" height="140" viewBox="0 0 140 140"><circle cx="70" cy="70" r="66" fill="#fff" stroke="#e6e8eb" stroke-width="2"/><path d="M4 70a66 66 0 0 0 132 0" fill="none" stroke="#4fbf1d" stroke-width="5"/><circle cx="70" cy="70" r="9" fill="none" stroke="#4fbf1d" stroke-width="3"/><g stroke="#4fbf1d" stroke-width="2.5"><path d="M70 61V46M70 79v15M61 70H46M79 70h15M64 64l-10-10M76 76l10 10M76 64l10-10M64 76l-10 10"/></g><g fill="#4fbf1d"><circle cx="70" cy="44" r="4"/><circle cx="70" cy="96" r="4"/><circle cx="44" cy="70" r="4"/><circle cx="96" cy="70" r="4"/><circle cx="52" cy="52" r="4"/><circle cx="88" cy="88" r="4"/><circle cx="88" cy="52" r="4"/><circle cx="52" cy="88" r="4"/></g></svg>
  <h4>Outsourcing</h4>
  <p class="para">Lorem Ipsum is simply dummy text of the printing and typesetting industry. Lorem Ipsum has been the industry's standard dummy text ever since the 1500s.</p>
  <div class="btn btn-green">View Details</div>
</div>
<div class="abs service" style="left:515px">
  <svg width="140" height="140" viewBox="0 0 140 140"><circle cx="70" cy="70" r="66" fill="#fff" stroke="#e6e8eb" stroke-width="2"/><path d="M4 70a66 66 0 0 1 132 0" fill="none" stroke="#1b6fd3" stroke-width="5"/><circle cx="70" cy="70" r="22" fill="none" stroke="#1b6fd3" stroke-width="3"/><circle cx="70" cy="70" r="8" fill="#1b6fd3"/><path d="M48 70a22 22 0 0 1 10-18l-4-4M92 70a22 22 0 0 1-10 18l4 4" stroke="#1b6fd3" stroke-width="3" fill="none"/></svg>
  <h4>Development</h4>
  <p class="para">Lorem Ipsum is simply dummy text of the printing and typesetting industry. Lorem Ipsum has been the industry's standard dummy text ever since the 1500s.</p>
  <div class="btn btn-blue">View Details</div>
</div>
<div class="abs service" style="left:716px">
  <svg width="140" height="140" viewBox="0 0 140 140"><circle cx="70" cy="70" r="66" fill="#fff" stroke="#e6e8eb" stroke-width="2"/><path d="M4 70a66 66 0 0 0 132 0" fill="none" stroke="#4fbf1d" stroke-width="5"/><rect x="48" y="50" width="44" height="34" fill="none" stroke="#4fbf1d" stroke-width="3"/><path d="M54 76l10-10 8 6 14-14" fill="none" stroke="#4fbf1d" stroke-width="3"/><path d="M60 92h20" stroke="#4fbf1d" stroke-width="3"/></svg>
  <h4>Business Analyst</h4>
  <p class="para">Lorem Ipsum is simply dummy text of the printing and typesetting industry. Lorem Ipsum has been the industry's standard dummy text ever since the 1500s.</p>
  <div class="btn btn-green">View Details</div>
</div>
<div class="abs service" style="left:918px">
  <svg width="140" height="140" viewBox="0 0 140 140"><circle cx="70" cy="70" r="66" fill="#fff" stroke="#e6e8eb" stroke-width="2"/><path d="M4 70a66 66 0 0 1 132 0" fill="none" stroke="#1b6fd3" stroke-width="5"/><rect x="46" y="50" width="48" height="34" fill="none" stroke="#1b6fd3" stroke-width="3"/><rect x="54" y="58" width="32" height="18" fill="#1b6fd3"/><path d="M58 96l12-12 12 12M70 84v-4" stroke="#1b6fd3" stroke-width="3" fill="none"/></svg>
  <h4>Training</h4>
  <p class="para">Lorem Ipsum is simply dummy text of the printing and typesetting industry. Lorem Ipsum has been the industry's standard dummy text ever since the 1500s.</p>
  <div class="btn btn-blue">View Details</div>
</div>

<!-- career -->
<section class="abs career"></section>
<div class="abs video" role="img" aria-label="Laptop with code on screen on a desk in a dim room"></div>
<div class="abs play"><svg width="34" height="38" viewBox="0 0 34 38"><polygon points="4,2 32,19 4,36" fill="#fff"/></svg></div>
<article class="abs career-box">
  <h2>Know About Your Carrer</h2>
  <p class="para">Lorem Ipsum is simply dummy text of the printing and typesetting industry. Lorem Ipsum has been the industry's standard dummy text ever since the 1500s.<br>Lorem Ipsum is simply dummy text of the printing and typesetting industry. Lorem Ipsum has been the industry's standard dummy text ever since the 1500s.Lorem Ipsum is simply dummy text of the printing and typesetting industry. Lorem Ipsum has been the industry's standard dummy text ever since the 1500s.<br>Lorem Ipsum is simply dummy text of the printing and typesetting industry. Lorem Ipsum has been the industry's standard dummy text ever since the 1500s.Lorem Ipsum is simply dummy text of the printing and typesetting industry. Lorem Ipsum has been the industry's standard dummy text ever since the 1500s.</p>
  <a>Know More &gt;&gt;</a>
</article>

<!-- news -->
<h2 class="abs section-title" style="top:3092px">Latest News</h2>
<p class="abs section-sub para" style="top:3148px">Sed ut perspiciatis unde omnis iste natus error sit voluptatem accusantium doloremque</p>

<article class="abs news" style="left:95px">
  <div class="news-img" role="img" aria-label="Modern glass office interior"></div>
  <div class="news-body"><div class="news-date">29/03/19</div><h5>Nemo enim ipsam voluptatem</h5><p class="para">Sed ut perspiciatis unde omnis iste natus error sit voluptatem accusantium doloremque laudan-tium totam rem aperiam, eaque ipsa quae .</p><div class="btn btn-blue">Read More</div></div>
</article>
<article class="abs news" style="left:441px">
  <div class="news-body"><div class="news-date">29/03/19</div><h5>Nemo enim ipsam voluptatem</h5><p class="para">Sed ut perspiciatis unde omnis iste natus error sit voluptatem accusantium doloremque laudan-tium totam rem aperiam, eaque ipsa quae .</p><div class="btn btn-blue">Read More</div></div>
  <div class="news-img" style="background:linear-gradient(135deg,#3a4048,#1f2328 60%,#2d3a44)" role="img" aria-label="Hands typing on a laptop keyboard"></div>
</article>
<article class="abs news" style="left:787px">
  <div class="news-img" style="background:linear-gradient(135deg,#d8dadc,#9aa2a8 55%,#6b737a)" role="img" aria-label="Colleagues working at computers in an office"></div>
  <div class="news-body"><div class="news-date">29/03/19</div><h5>Nemo enim ipsam voluptatem</h5><p class="para">Sed ut perspiciatis unde omnis iste natus error sit voluptatem accusantium doloremque laudan-tium totam rem aperiam, eaque ipsa quae .</p><div class="btn btn-blue">Read More</div></div>
</article>

<!-- request a call -->
<div class="abs request-photo" role="img" aria-label="Bright meeting room with people working at a long table"></div>
<h2 class="abs request-title">Request a Call</h2>
<p class="abs request-sub">Just fill in the form &amp; send us. We will get back to you within 24 hours.</p>
<div class="abs field" style="left:95px;top:3885px;width:284px">Name *</div>
<div class="abs field" style="left:389px;top:3885px;width:284px">Email Address *</div>
<div class="abs field" style="left:95px;top:3939px;width:284px">Subject <svg width="8" height="6"><polygon points="0,0 8,0 4,6" fill="#1b6fd3"/></svg></div>
<div class="abs field" style="left:389px;top:3939px;width:284px">Phone No *</div>
<div class="abs field area" style="left:95px;top:3993px;width:578px;height:138px">Message</div>
<div class="abs btn btn-blue send">Send Message</div>
<div class="abs call-alt">Or Call Us <span>+1 (001) 123 45 678 90</span></div>

<!-- partners -->
<section class="abs partners"></section>
<div class="abs arrow-btn" style="left:33px"><svg width="8" height="10"><path d="M7 1L2 5l5 4" fill="none" stroke="#666" stroke-width="1.5"/></svg></div>
<div class="abs arrow-btn" style="left:1142px"><svg width="8" height="10"><path d="M1 1l5 4-5 4" fill="none" stroke="#666" stroke-width="1.5"/></svg></div>
<div class="abs partner-row">
  <div class="partner-shape" style="width:66px"></div>
  <div class="partner-shape" style="width:58px"></div>
  <div class="partner-shape" style="width:56px"></div>
  <div class="partner-shape" style="width:86px;height:12px"></div>
  <div class="partner-shape" style="width:46px"></div>
  <div class="partner-shape" style="width:44px;height:36px;border-radius:50%"></div>
  <div class="partner-shape" style="width:70px;height:12px"></div>
  <div class="partner-shape" style="width:34px;height:34px;border-radius:50%"></div>
  <div class="partner-shape" style="width:90px;height:12px"></div>
  <div class="partner-shape" style="width:32px;height:32px"></div>
  <div class="partner-shape" style="width:44px"></div>
</div>

<!-- footer -->
<footer class="abs footer"></footer>
<div class="abs" style="left:95px;top:4512px;width:260px">
  <div class="foot-h">About Us</div>
  <p class="foot-text" style="margin-top:26px">Lorem Ipsum is simply dummy text of the printing and typesetting industry. Lorem Ipsum has been the industry's standard dummy text ever since the1500s.</p>
</div>
<div class="abs follow" style="color:#fff">Follow Us : <span class="social"></span><span class="social"></span><span class="social"></span><span class="social"></span></div>
<div class="abs" style="left:430px;top:4512px">
  <div class="foot-h">Site Map</div>
  <ul class="foot-list" style="margin-top:12px"><li>About Us</li><li>Services</li><li>Partner</li><li>Career</li><li>Contact</li></ul>
</div>
<div class="abs" style="left:610px;top:4512px;width:220px">
  <div class="foot-h">Contact Us</div>
  <div style="margin-top:24px">
    <div class="contact-row"><svg width="14" height="18" viewBox="0 0 14 18"><path d="M7 1C4 1 1 3 1 7c0 4 6 10 6 10s6-6 6-10c0-4-3-6-6-6z" fill="none" stroke="#fff" stroke-width="1.5"/><circle cx="7" cy="7" r="2" fill="#fff"/></svg><span>152 Lorem ipsum, Dolor Lorem<br>Lorem ipsum14582</span></div>
    <div class="contact-row"><svg width="14" height="14" viewBox="0 0 14 14"><path d="M2 1h3l1 3-2 1c1 2 2 3 4 4l1-2 3 1v3c0 1-1 2-2 2C5 13 1 9 1 3c0-1 0-2 1-2z" fill="none" stroke="#fff" stroke-width="1.3"/></svg><span>+1 (001) 123 45 678 90</span></div>
    <div class="contact-row"><svg width="14" height="12" viewBox="0 0 14 12"><rect x="1" y="1" width="12" height="10" fill="none" stroke="#fff" stroke-width="1.3"/><path d="M1 1l6 5 6-5" fill="none" stroke="#fff" stroke-width="1.3"/></svg><span>index@vendimark-mail.de</span></div>
  </div>
</div>
<div class="abs" style="left:892px;top:4512px;width:230px">
  <div class="foot-h">Latest News</div>
  <div style="margin-top:18px">
    <div class="mini-news"><div class="mini-thumb" role="img" aria-label="Office interior"></div><p>Lorem Ipsum is simply<small>May 10, 2019</small></p></div>
    <div class="mini-news"><div class="mini-thumb" role="img" aria-label="Laptop on desk"></div><p>Lorem Ipsum is simply<small>May 10, 2019</small></p></div>
    <div class="mini-news"><div class="mini-thumb" role="img" aria-label="Team at computers"></div><p>Lorem Ipsum is simply<small>May 10, 2019</small></p></div>
  </div>
</div>
<div class="abs copyright">Copyright © 2019 VendiMark. All Rights Reserved</div>

</body>
</html>
```